Business card design needed

the business is HR Consulting, but its for SME businesses who cant afford a permanent HR person. We sell an HR info system to help them meet minimum employment legislation but with this hope they then require us on a monthly subscription to phone or email us for HR advice. We are HR qualified mums working from home

So we will be partners to HR and Payroll systems known as unify HR and Tally

Target Market(s)

Small to medium businesses so not black and overly corporate, but having said that many are accounting businesses

Industry/Entity Type

Business

Contact Information for Business Card

Name of the company: Maple HR

Me:Marta Oldenbrook
Title:Managing Director

m: 0438 615 209
e: marta@maplehr.com.au
w: www.maplehr.com.au

What we do: HR Consulting, HR Systems and support, Payroll Advice

Requirements
Nice to have
• there is a company already out there known as Harbor professionals. I like the leaves at the end as I wanted something different like this to the usual business logos but still professional. I wanted a symbol to show calm, positive, ease flow going up ,etc. but realise they have the leaves and possibly cant copy, or can we?..( kite??, something calm and positive)dont know!!. Green and blue needed to be in it as nature and calm as well. I love the colours of www.staffingfundco.com ( attached the colours), as well as the calm wave line underneath. have a look as while they use green and blue I loved the purple colour thrown in there.Green and blue on their own are so overused. I want vibrant. I want double sided and when on a table I want it to stand out so maybe the purple colour (as per the colours on the fund website) solid on one side with just the 3 services we provide and personal and company name on front but need some creativity from you guys.

```html
<!DOCTYPE html>
<html lang="en">
<head>
<meta charset="utf-8">
<title>Maple HR – Business Card</title>
<link rel="stylesheet" href="https://fonts.googleapis.com/css2?family=EB+Garamond:ital,wght@0,400;1,400&display=swap">
<style>
  :root {
    --green-deep: #66b400;
    --green-bright: #80ff00;
    --green-mid: #72d400;
    --lime-ring: #8cff00;
    --blue: #2850ff;
    --brand-blue: #1a1fd6;
    --ink-white: #ffffff;
    --foliage: #4f9a5e;
  }
  * { margin: 0; padding: 0; box-sizing: border-box; }
  html, body {
    width: 1200px;
    height: 741px;
    overflow: hidden;
    background: #ffffff;
  }
  .card {
    position: relative;
    width: 1200px;
    height: 741px;
    overflow: hidden;
    background: linear-gradient(180deg,
      var(--green-deep) 0%,
      var(--green-mid) 22%,
      var(--green-bright) 48%,
      var(--green-mid) 78%,
      var(--green-deep) 100%);
    font-family: "EB Garamond", Garamond, serif;
    color: var(--ink-white);
  }
  .corner-arc {
    position: absolute;
    left: 0;
    top: 0;
  }
  .brand-name {
    position: absolute;
    right: 30px;
    top: 22px;
    font-size: 72px;
    font-weight: 400;
    font-style: normal;
    color: var(--brand-blue);
    letter-spacing: 1px;
    line-height: 1;
  }
  .tree-area {
    position: absolute;
    left: 650px;
    top: 228px;
    width: 550px;
    height: 513px;
    border-radius: 60% 40% 0 0 / 55% 45% 0 0;
    background: radial-gradient(ellipse at 65% 55%,
      rgba(79, 154, 94, 0.55) 0%,
      rgba(79, 154, 94, 0.3) 45%,
      rgba(79, 154, 94, 0) 75%);
  }
  .person {
    position: absolute;
    left: 184px;
    top: 212px;
    font-style: italic;
  }
  .person-name {
    display: inline-block;
    font-size: 54px;
    font-weight: 400;
    line-height: 1.05;
    border-bottom: 2px solid var(--ink-white);
    padding-bottom: 2px;
  }
  .person-title {
    font-size: 37px;
    line-height: 1.15;
    margin-top: 2px;
  }
  .contact {
    position: absolute;
    left: 178px;
    top: 372px;
    list-style: none;
    font-style: italic;
    font-size: 28px;
    line-height: 42px;
  }
  .services {
    position: absolute;
    left: 175px;
    top: 517px;
    font-style: italic;
    font-size: 28px;
    line-height: 43px;
  }
</style>
</head>
<body>
  <div class="card">
    <svg class="corner-arc" width="330" height="250" viewBox="0 0 330 250" aria-hidden="true">
      <circle cx="-32" cy="-43" r="292" fill="var(--lime-ring)"/>
      <circle cx="-32" cy="-43" r="246" fill="var(--blue)"/>
    </svg>

    <div class="brand-name">Maple HR</div>

    <div class="tree-area" role="img" aria-label="Soft green illustration of a leafy tree branch rising from the lower right corner"></div>

    <div class="person">
      <div class="person-name">Marta Oldenbrook</div>
      <div class="person-title">Managing Director</div>
    </div>

    <ul class="contact">
      <li>m : 0438 615 209</li>
      <li>e : marta@maplehr.com.au</li>
      <li>w : www.maplehr.com.au</li>
    </ul>

    <p class="services">What we do : HR Consulting, HR Systems<br>and support, Payroll Advice</p>
  </div>
</body>
</html>
```